Invitation - Photos with Santa

We’re doing an event this Christmas for people get photos with Santa.
It’ll be a postcard that we mail to people we know.
Size: 5 x 7, two sided
Details for back of postcard:
Saturday, December 4
10 a.m. - 12 p.m.
18457 Colvin Ln.
Larkmoor, WV 44873
The company putting it on is Brightwick. I’ve got a million logo formats so just let me know what you need.
In terms of theme/look/feel for the front of card, I’m a little stuck so I’m open to whatever.
-Skip the line?
-Private Santa party?
-Screw the mall?
Attached is an old one we used last time time we did it.
Let me know if there are any questions!
People I know personally, people with kids, people who private photo with Santa without having to go to the mall

```html
<!DOCTYPE html>
<html lang="en">
<head>
<meta charset="utf-8">
<title>Brightwick – Photos with Santa Postcard</title>
<link href="https://fonts.googleapis.com/css2?family=Bebas+Neue&family=Kaushan+Script&family=Open+Sans:wght@300;400&family=Poppins:wght@700&family=Yellowtail&display=swap" rel="stylesheet">
<style>
  :root {
    --backdrop: #bcbdc0;
    --red: #d1222a;
    --deep-red: #c41f27;
    --orange: #e9582b;
    --cream: #ebe4d4;
    --frame: #f1eee2;
    --ink: #111111;
    --rule: #9a9a9a;
    --white: #ffffff;
  }
  * { margin: 0; padding: 0; box-sizing: border-box; }
  html, body { width: 924px; height: 1200px; overflow: hidden; }
  body { background: var(--backdrop); position: relative; font-family: "Open Sans", sans-serif; }

  .postcard { position: absolute; left: 120px; width: 672px; height: 480px; box-shadow: 6px 8px 10px rgba(0,0,0,0.35); overflow: hidden; }

  /* Front */
  .postcard-front { top: 91px; background: radial-gradient(ellipse at 30% 40%, #414141 0%, #262626 55%, #161616 100%); }
  .script { font-family: "Yellowtail", "Kaushan Script", cursive; font-weight: 400; }
  .headline-peace { position: absolute; left: 36px; top: 16px; font-size: 104px; color: var(--red); line-height: 1; transform: rotate(-6deg); transform-origin: left center; text-shadow: 2px 3px 4px rgba(0,0,0,0.5); white-space: nowrap; }
  .headline-amp { position: absolute; left: 140px; top: 118px; font-size: 70px; color: var(--red); line-height: 1; }
  .headline-joy { position: absolute; left: 28px; top: 186px; width: 264px; text-align: center; font-family: "Poppins", sans-serif; font-weight: 700; font-size: 118px; letter-spacing: -4px; color: var(--red); line-height: 1; text-shadow: 2px 3px 4px rgba(0,0,0,0.5); }
  .front-tagline { position: absolute; left: 28px; top: 330px; width: 264px; text-align: center; font-family: "Bebas Neue", sans-serif; font-size: 38px; color: var(--cream); letter-spacing: 0.5px; line-height: 1; }
  .brand { position: absolute; display: flex; flex-direction: column; align-items: center; gap: 6px; }
  .brand-dot { width: 34px; height: 34px; border-radius: 50%; background: var(--orange); }
  .brand-name { font-family: "Open Sans", sans-serif; font-weight: 400; font-size: 15px; color: var(--orange); letter-spacing: 0.5px; }
  .front-brand { left: 100px; top: 398px; width: 120px; }

  .photo-frame { position: absolute; left: 332px; top: 28px; width: 332px; height: 432px; background: var(--frame); padding: 9px; transform: rotate(1.2deg); box-shadow: 4px 6px 10px rgba(0,0,0,0.55); }
  .photo-area { width: 100%; height: 100%; background: linear-gradient(160deg, #f3f1ec 0%, #dcd6cf 40%, #8c2f30 62%, #2b2a2e 85%, #56606a 100%); }

  /* Back */
  .postcard-back { top: 627px; background: var(--white); }
  .invite-column { position: absolute; left: 0; top: 0; width: 345px; height: 480px; text-align: center; }
  .invite-column > * { position: absolute; left: 0; width: 345px; }
  .invite-lead { top: 24px; font-size: 19px; line-height: 25px; color: var(--ink); letter-spacing: 0.3px; }
  .invite-details { top: 82px; font-weight: 300; font-size: 23px; line-height: 29px; color: var(--deep-red); }
  .invite-for { top: 166px; font-size: 46px; color: var(--deep-red); line-height: 1; }
  .invite-title { top: 236px; font-family: "Bebas Neue", sans-serif; font-weight: 400; font-size: 46px; color: var(--ink); line-height: 1; }
  .invite-address { top: 292px; font-size: 14px; color: var(--deep-red); }
  .invite-note { top: 326px; font-size: 17px; line-height: 21px; color: var(--ink); }
  .lockup { top: 402px; display: flex; justify-content: center; align-items: center; gap: 8px; }
  .lockup-peace { font-size: 54px; color: var(--red); line-height: 1; transform: rotate(-5deg); }
  .lockup-amp { font-size: 40px; color: var(--orange); line-height: 1; }
  .lockup-joy { font-family: "Poppins", sans-serif; font-weight: 700; font-size: 46px; letter-spacing: -2px; color: var(--red); line-height: 1; }
  .address-rule { position: absolute; left: 358px; top: 24px; width: 1px; height: 435px; background: var(--rule); }
  .back-brand { left: 382px; top: 28px; width: 110px; }
</style>
</head>
<body>
  <section class="postcard postcard-front">
    <div class="headline-peace script">Peace</div>
    <div class="headline-amp script">&amp;</div>
    <div class="headline-joy">JOY</div>
    <div class="front-tagline">Private Santa Party</div>
    <div class="brand front-brand">
      <span class="brand-dot"></span>
      <span class="brand-name">BRIGHTWICK</span>
    </div>
    <div class="photo-frame">
      <div class="photo-area" role="img" aria-label="Photo of two children in Santa hats wrapped in strings of Christmas lights"></div>
    </div>
  </section>

  <section class="postcard postcard-back">
    <div class="invite-column">
      <p class="invite-lead">THE BRIGHTWICK TEAM<br>INVITES YOU TO</p>
      <p class="invite-details">JOIN US<br>Saturday, December 4<br>10 a.m. - 12 p.m.</p>
      <p class="invite-for script">for</p>
      <h1 class="invite-title">PHOTOS WITH SANTA</h1>
      <p class="invite-address">18457 Colvin Ln. Larkmoor, WV 44873</p>
      <p class="invite-note">Prepare to skip the lines<br>and capture memorable photos<br>for the holiday season</p>
      <div class="lockup">
        <span class="lockup-peace script">Peace</span>
        <span class="lockup-amp script">&amp;</span>
        <span class="lockup-joy">JOY</span>
      </div>
    </div>
    <div class="address-rule"></div>
    <div class="brand back-brand">
      <span class="brand-dot"></span>
      <span class="brand-name">BRIGHTWICK</span>
    </div>
  </section>
</body>
</html>
```